a business advisory consulting website

I need a website 3-5 pages to sell my professional services in IT and Project management Consulting. My company name is Northwell Strategy Consulting. I want it to be device friendly and easy to navigate for the busy executive however intriguing enough.
I have attached some info I drafted on About the company and personal Bio. Also there is a website that I really like that I have attached the initial site pdf and websites that I like are here: https://quillmarshcapital.example, https://tandermoviews.example, https://www.felkinlearningconsulting.example as examples. Thanks
Updates

Hi Designers, I have uploaded the logo in 3D .png format, to assist in the web design.

Target Market(s)

B2B, governments, IT companies, Project Management companies and Consulting firms, small medium enterprises to large corporate enterprises.

Industry/Entity Type

It Professional

Coding

Coded - Design and coding required

Number of Pages Required

5+ page

Font styles to use
Sans Serif

Requirements
Must have
• Home, About company, the team, what we do and contact us
Nice to have
• Blog
Should not have
• pop ups, flash

```html
<!DOCTYPE html>
<html lang="en">
<head>
<meta charset="utf-8">
<title>Northwell Strategy Consulting</title>
<link href="https://fonts.googleapis.com/css2?family=Roboto:ital,wght@0,400;0,500;0,700;1,400&display=swap" rel="stylesheet">
<style>
:root{
  --red:#e3262a;
  --navy:#232a4b;
  --navy-soft:#2f3a63;
  --ink:#1d1d1d;
  --grey:#5b5b5b;
  --field:#efefef;
  --white:#fff;
}
*{margin:0;padding:0;box-sizing:border-box}
html,body{width:1200px;height:3397px;overflow:hidden}
body{position:relative;font-family:'Roboto',sans-serif;color:var(--ink);background:var(--white)}
.abs{position:absolute}
.topbar{left:0;top:0;width:1200px;height:32px;background:var(--navy);color:var(--white);font-size:13px}
.topbar span{position:absolute;top:8px;display:flex;align-items:center;gap:6px}
.social-sq{display:inline-block;width:20px;height:20px;background:var(--red);border-radius:2px}
.nav{left:0;top:32px;width:1200px;height:83px;background:var(--white)}
.brand{position:absolute;display:flex;align-items:center;gap:8px;font-weight:700;font-size:22px;color:var(--red);text-transform:uppercase;line-height:1}
.brand i{display:block;width:26px;height:26px;background:var(--red)}
.menu{position:absolute;right:122px;top:32px;display:flex;gap:38px;font-size:16px;font-weight:500}
.menu a{color:var(--ink);text-decoration:none}
.menu a.active{color:var(--red)}
.hero{left:0;top:115px;width:1200px;height:496px;background:linear-gradient(180deg,#0f2b7a 0%,#12307e 45%,#0b1533 62%,#5c3a3c 78%,#1a2a5a 100%);color:var(--white);text-align:center}
.hero h1{position:absolute;top:84px;width:100%;font-size:29px;font-weight:500}
.hero p{position:absolute;top:141px;width:100%;font-size:27px}
.dots{position:absolute;top:447px;left:565px;display:flex;gap:18px}
.dots b{width:11px;height:11px;background:var(--white);transform:rotate(45deg)}
.dots b.on{background:var(--red)}
.h2{position:absolute;width:100%;text-align:center;font-size:38px;font-weight:500}
.h2 em{font-style:normal;color:var(--red)}
.intro{left:123px;top:748px;width:955px;font-size:13.4px;line-height:21px;text-align:justify;text-align-last:center}
.card-img{position:absolute;width:291px;height:220px}
.card-title{position:absolute;width:291px;text-align:center;color:var(--red);font-size:21px;font-weight:500}
.card-text{position:absolute;width:291px;text-align:center;font-size:14px;line-height:21px;color:#333;padding:0 6px}
.team{left:0;top:1308px;width:1200px;height:318px;background:linear-gradient(90deg,#2a3560,#3b4878 50%,#2a3560)}
.team-photo{position:absolute;left:186px;top:53px;width:190px;height:224px;border-radius:12px;background:linear-gradient(180deg,#e9e9ec,#cfd1d6)}
.team-name{position:absolute;left:415px;top:80px;color:var(--white);font-size:21px;font-weight:700}
.team-role{position:absolute;left:415px;top:112px;color:var(--white);font-size:15px;font-style:italic}
.team-bio{position:absolute;left:415px;top:148px;width:612px;color:var(--white);font-size:12.6px;line-height:19.3px;text-align:justify}
.arrows{position:absolute;left:957px;top:78px;display:flex;gap:6px}
.arrows span{width:32px;height:28px;background:#8e93a8;display:flex;align-items:center;justify-content:center}
.blog-img{position:absolute;width:291px;height:174px}
.blog-title{position:absolute;color:var(--red);font-size:17px;font-weight:500}
.blog-meta{position:absolute;color:#777;font-size:13px;font-style:italic}
.blog-text{position:absolute;width:270px;font-size:16px;line-height:24px;color:#222}
.btn{position:absolute;background:var(--navy);color:var(--white);font-weight:500;font-size:15px;border-radius:24px;display:flex;align-items:center;justify-content:center}
.subscribe{left:0;top:2237px;width:1200px;height:236px;background:linear-gradient(90deg,#2d3a6a,#3a4a80 50%,#2d3a6a)}
.subscribe h3{position:absolute;top:72px;width:100%;text-align:center;color:var(--white);font-size:23px;font-weight:500}
.sub-field{position:absolute;top:124px;height:50px;background:var(--white);font-size:16px;color:#444;padding:15px 30px}
.feat-icon{position:absolute;left:123px;width:76px;height:76px;border:2px solid var(--red);border-radius:50%;display:flex;align-items:center;justify-content:center}
.feat-title{position:absolute;left:223px;font-size:16px;font-weight:700;color:#1f2440}
.feat-text{position:absolute;left:223px;width:380px;font-size:14px;line-height:21px;color:#222}
.contact-h{left:692px;top:2531px;color:var(--red);font-size:25px;font-weight:700}
.field{position:absolute;left:692px;width:386px;background:var(--field);font-size:14px;color:#555;padding:16px 26px}
.footer{left:0;top:3037px;width:1200px;height:360px;background:var(--navy);color:var(--white);font-size:13.5px}
.footer h4{position:absolute;top:61px;color:var(--red);font-size:15px;font-weight:500}
.footer ul{position:absolute;list-style:none;line-height:22.5px}
.lbl{color:var(--red)}
.circ{display:inline-block;width:28px;height:28px;border-radius:50%;background:var(--red)}
</style>
</head>
<body>

<div class="abs topbar">
  <span style="left:122px"><svg width="14" height="14" viewBox="0 0 14 14"><circle cx="7" cy="7" r="6" fill="none" stroke="#e3262a" stroke-width="1.6"/><path d="M7 3v4l3 2" stroke="#e3262a" stroke-width="1.6" fill="none"/></svg>Mon-Fri 8:00am - 4:30pm</span>
  <span style="left:614px"><svg width="16" height="12" viewBox="0 0 16 12"><rect width="16" height="12" rx="2" fill="#e3262a"/><path d="M1 1l7 6 7-6" stroke="#232a4b" stroke-width="1.4" fill="none"/></svg>hello@quillmarshcapital.example</span>
  <span style="left:851px"><svg width="14" height="14" viewBox="0 0 14 14"><path d="M3 1l3 3-2 2c1 2 2 3 4 4l2-2 3 3-2 3C5 13 1 9 0 3z" fill="#e3262a"/></svg>+ 254 700 410 118</span>
  <span style="left:1003px;gap:8px"><i class="social-sq"></i><i class="social-sq"></i><i class="social-sq"></i></span>
</div>

<header class="abs nav">
  <div class="brand" style="left:123px;top:28px"><i></i>Northwell Strategy</div>
  <nav class="menu">
    <a class="active" href="#">HOME</a><a href="#">ABOUT US</a><a href="#">WHAT WE DO</a><a href="#">OUR TEAM</a><a href="#">CONTACT US</a>
  </nav>
</header>

<section class="abs hero" role="img" aria-label="Night harbour skyline with a lit arch bridge and opera house reflected in the water">
  <h1>EXCELLENCE | EXPERTISE | ENTHUSIASM</h1>
  <p>A Strategy and Management Consulting Enterprise</p>
  <div class="dots"><b></b><b class="on"></b><b></b></div>
</section>

<h2 class="h2" style="top:670px"><em>Welcome to</em> Northwell Strategy</h2>
<p class="abs intro">We are a specialist operational excellence firm, delivering consulting and advisory services in six core capabilities, across all industries and all business lines to improve performance, efficiency, profitability, automation and scalability, for clients across Australia. We approach business consulting differently, with a Genuine Client Partnership model that builds client capability and rightsized solutions for the client.</p>

<div class="card-img" style="left:123px;top:861px;background:linear-gradient(135deg,#d9d9d9,#9d9d9d)" role="img" aria-label="Businessman facing a wall of sketched business charts"></div>
<div class="card-img" style="left:455px;top:861px;background:linear-gradient(135deg,#2c4a7a,#8ba3c3)" role="img" aria-label="Hand moving a chess piece on a board"></div>
<div class="card-img" style="left:787px;top:861px;background:linear-gradient(135deg,#7a5a3c,#d8b27a 50%,#3a4258)" role="img" aria-label="Stacked coins with financial chart overlay"></div>
<div class="card-title" style="left:123px;top:1118px">Market-Entry</div>
<div class="card-title" style="left:455px;top:1118px">Business Analytics</div>
<div class="card-title" style="left:787px;top:1118px">Financial Services</div>
<p class="card-text" style="left:123px;top:1161px">We develop concept-models and strategy maps for firms that seek marketentry into Africa. We analyze and assess African markets...</p>
<p class="card-text" style="left:455px;top:1161px">We develop concept-models and strategy maps for firms that seek marketentry into Africa. We analyze and assess African markets...</p>
<p class="card-text" style="left:787px;top:1161px">We develop concept-models and strategy maps for firms that seek marketentry into Africa. We analyze and assess African markets...</p>

<section class="abs team" role="img" aria-label="Silhouettes of business people in an office, blue overlay">
  <div class="team-photo" role="img" aria-label="Portrait of the managing principal"></div>
  <div class="team-name">DANIEL OKOTH</div>
  <div class="team-role">Managing Principal</div>
  <p class="team-bio">Daniel is a finance and strategy professional with extensive work experience workingin the financial services industry for large multinational corporations in Kenya.Daniel has over seven years working in the financial services industry having worked in the Vehicle and Asset Finance division as a Business Development Manager at Meridian Bank Group,known as Meridian Bank Kenya responsible for structuring finance facilities for major motor-vehicle &amp; insurance dealerships across the country.</p>
  <div class="arrows">
    <span><svg width="10" height="12" viewBox="0 0 10 12"><path d="M7 1L2 6l5 5" stroke="#fff" stroke-width="2" fill="none"/></svg></span>
    <span><svg width="10" height="12" viewBox="0 0 10 12"><path d="M3 1l5 5-5 5" stroke="#fff" stroke-width="2" fill="none"/></svg></span>
  </div>
</section>

<h2 class="h2" style="top:1680px;font-size:30px;font-weight:700"><em>LATEST</em> BLOG</h2>
<div class="blog-img" style="left:123px;top:1764px;background:linear-gradient(135deg,#e8e2dc,#b7a9b8)" role="img" aria-label="Girl using a tablet at a desk"></div>
<div class="blog-img" style="left:455px;top:1764px;background:linear-gradient(180deg,#e8a049,#a8532e 60%,#3c2a22)" role="img" aria-label="City skyline at sunset"></div>
<div class="blog-img" style="left:787px;top:1764px;background:linear-gradient(135deg,#6f8a5e,#d9d2c7 55%,#a0593a)" role="img" aria-label="Woman working on a laptop by a window"></div>
<div class="blog-title" style="left:121px;top:1968px">Guide for Consulting Business</div>
<div class="blog-title" style="left:453px;top:1968px">Decision Making in Certainty</div>
<div class="blog-title" style="left:785px;top:1968px">Post COVID-19 World</div>
<div class="blog-meta" style="left:121px;top:2004px">Posted 22 July 2020, by Mara Ellison</div>
<div class="blog-meta" style="left:453px;top:2004px">Posted 22 July 2020, by Mara Ellison</div>
<div class="blog-meta" style="left:785px;top:2004px">Posted 22 July 2020, by Mara Ellison</div>
<p class="blog-text" style="left:121px;top:2027px">Many parents across the globe are facing the challenge of having to ...</p>
<p class="blog-text" style="left:453px;top:2027px">Many parents across the globe are facing the challenge of having to ...</p>
<p class="blog-text" style="left:785px;top:2027px">Many parents across the globe are facing the challenge of having to ...</p>
<div class="btn" style="left:527px;top:2126px;width:146px;height:42px">VIEW ALL</div>

<section class="abs subscribe" role="img" aria-label="Business handshake, blue overlay">
  <h3>Want to get Latest updates? Subscribe Now</h3>
  <div class="sub-field" style="left:264px;width:306px">Enter Your Name</div>
  <div class="sub-field" style="left:574px;width:306px">Enter Email Address</div>
  <div class="abs" style="left:884px;top:124px;width:51px;height:50px;background:var(--red);display:flex;align-items:center;justify-content:center"><svg width="14" height="22" viewBox="0 0 14 22"><path d="M3 2l9 9-9 9" stroke="#fff" stroke-width="2.6" fill="none"/></svg></div>
</section>

<div class="feat-icon" style="top:2534px"><svg width="36" height="40" viewBox="0 0 36 40" fill="none" stroke="#e3262a" stroke-width="2"><rect x="6" y="3" width="24" height="34" rx="2"/><path d="M11 11h14M11 17h14M11 23h14M11 29h9"/></svg></div>
<div class="feat-title" style="top:2541px">ETHICS &amp; INTEGRITY</div>
<p class="feat-text" style="top:2567px">We value ethics and integrity when engaging all our clients and the businesses they operate.</p>

<div class="feat-icon" style="top:2646px"><svg width="36" height="40" viewBox="0 0 36 40" fill="none" stroke="#e3262a" stroke-width="2"><path d="M10 4h16v10a8 8 0 01-16 0zM10 7H4c0 6 3 8 6 8M26 7h6c0 6-3 8-6 8M18 22v8M11 36h14l-2-6H13z"/></svg></div>
<div class="feat-title" style="top:2653px">100% EFFICIENCY</div>
<p class="feat-text" style="top:2679px">We strive for 100% efficiency to optimize the operational structures to maximize revenue and returns.</p>

<div class="feat-icon" style="top:2757px"><svg width="38" height="38" viewBox="0 0 38 38" fill="none" stroke="#e3262a" stroke-width="2"><path d="M17 5a13 13 0 1013 13H17z"/><path d="M21 2v12h12A12 12 0 0021 2z"/><circle cx="28" cy="29" r="6"/></svg></div>
<div class="feat-title" style="top:2764px">GROW AND SCALE</div>
<p class="feat-text" style="top:2790px">We exist to help grow and scale business operations, rationalize costs for startups, and SMEs.</p>

<div class="feat-icon" style="top:2869px"><svg width="38" height="36" viewBox="0 0 38 36" fill="none" stroke="#e3262a" stroke-width="2"><rect x="3" y="4" width="20" height="14" rx="3"/><path d="M8 18l-2 6 7-6"/><rect x="17" y="14" width="18" height="13" rx="3"/><path d="M30 27l2 5-6-5"/></svg></div>
<div class="feat-title" style="top:2876px">BUILD RELATIONSHIP</div>
<p class="feat-text" style="top:2902px">We manage long-term relationships with clients by offering timely feedback on all engagements.</p>

<h3 class="abs contact-h">CONTACT US</h3>
<div class="field" style="top:2586px;height:50px">Enter Full Name</div>
<div class="field" style="top:2647px;height:50px">Enter Email Address</div>
<div class="field" style="top:2707px;height:50px">Enter Phone Number</div>
<div class="field" style="top:2768px;height:137px">Type Message</div>
<div class="btn" style="left:692px;top:2925px;width:146px;height:43px">SUBMIT</div>

<footer class="abs footer">
  <div class="brand" style="left:123px;top:80px"><i></i>Northwell Strategy</div>
  <div class="abs" style="left:123px;top:146px;display:flex;gap:12px"><i class="circ"></i><i class="circ"></i><i class="circ"></i></div>
  <p class="abs" style="left:122px;top:190px;line-height:19px">Northwell Strategy © Copyright 2020.<br>All Rights Reserved.</p>

  <h4 style="left:437px">QUICK LINKS</h4>
  <ul style="left:437px;top:91px"><li>Home</li><li>About Us</li><li>What We Do</li><li>Our Team</li><li>Blog</li></ul>

  <h4 style="left:643px">INFO LINKS</h4>
  <ul style="left:643px;top:91px"><li>Terms and Conditions</li><li>Privacy Policy</li><li>Contact Us</li></ul>

  <h4 style="left:855px">CONTACT INFO</h4>
  <ul style="left:855px;top:91px">
    <li><span class="lbl">Phone:</span> + 254 700 410 118</li>
    <li style="padding-left:45px">+ 254 700 582 264</li>
    <li><span class="lbl">Email:</span> hello@quillmarshcapital.example</li>
    <li style="margin-top:22px;line-height:20px"><span class="lbl">Address:</span><br>12th Floor, Wing C,<br>Harbourline Towers, Cedar Lane</li>
  </ul>
</footer>

</body>
</html>
```